Open Orchard

We need a book cover design for a new company based in Atlanta called Bramwell Counseling. I am a psychologist. My company does seminars and provides counseling to couples struggling in their marriage and questioning whether to continue. We would like to see designs that communicates peace love and happiness,

Please make sure the the design is ready for print including front, back, and spine. File needs to be an editable layered PSD file. Back cover should include space to add the isbn,bar code, bio picture, and testimonials. Use high quality stock photo. The size is 6″ x 9″ . Name should be listed as Dr. Megan Trabert PhD

Reason: The back cover and spine needs to be included

Industry/Entity Type

It Company

```html
<!DOCTYPE html>
<html lang="en">
<head>
<meta charset="utf-8">
<title>Open Orchard — Book Cover</title>
<link rel="stylesheet" href="https://fonts.googleapis.com/css2?family=Advent+Pro:wght@200;300;400&family=Great+Vibes&family=Tinos:ital@0;1&display=swap">
<style>
  :root {
    --backdrop: #dcdcdd;
    --cover-light: #f7f6fa;
    --cover-mid: #e7e5ee;
    --cover-shade: #d6d4de;
    --glow-blue: rgba(186, 214, 255, 0.55);
    --glow-violet: rgba(226, 200, 255, 0.45);
    --silver-top: #cfd6de;
    --silver-mid: #7d8894;
    --silver-dark: #4f5964;
    --ink: #3f4348;
    --ink-soft: #6b6e74;
    --ring-light: #eeeae2;
    --ring-mid: #c9c3b6;
    --photo-tone: #8a7f76;
  }
  * { box-sizing: border-box; margin: 0; padding: 0; }
  html, body {
    width: 1200px; height: 900px; overflow: hidden;
    background: var(--backdrop);
  }
  .book-spread {
    position: absolute; left: 175px; top: 150px;
    width: 850px; height: 600px;
    display: flex;
    box-shadow: 0 18px 40px rgba(0,0,0,0.18);
  }
  .panel {
    position: relative; height: 600px; overflow: hidden;
    background:
      radial-gradient(circle at 55% 30%, var(--glow-blue), transparent 40%),
      radial-gradient(circle at 30% 70%, var(--glow-violet), transparent 45%),
      linear-gradient(160deg, var(--cover-light), var(--cover-mid) 60%, var(--cover-shade));
  }
  .back-cover { width: 400px; }
  .spine { width: 50px; border-left: 1px solid rgba(0,0,0,0.06); border-right: 1px solid rgba(0,0,0,0.08); }
  .front-cover { width: 400px; }

  .silver-text {
    font-family: "Advent Pro", sans-serif;
    font-weight: 300;
    color: var(--silver-mid);
    background: linear-gradient(180deg, var(--silver-top), var(--silver-mid) 55%, var(--silver-dark));
    -webkit-background-clip: text; background-clip: text;
    -webkit-text-fill-color: transparent;
  }

  /* Front */
  .front-title {
    position: absolute; left: 22px; right: 22px; top: 50px;
    line-height: 0.95; font-size: 82px; font-weight: 300;
    white-space: nowrap;
  }
  .front-title span { display: block; }
  .front-title .line-one { letter-spacing: 22px; }
  .front-title .line-two { letter-spacing: 1px; }
  .front-tagline {
    position: absolute; left: 0; right: 0; top: 232px; text-align: center;
    font-family: "Great Vibes", cursive; font-size: 26px;
    color: var(--ink-soft); letter-spacing: 1px;
  }
  .rings-photo {
    position: absolute; left: 60px; top: 360px; width: 280px; height: 120px;
    border-radius: 50%;
    background: radial-gradient(ellipse at 50% 45%, var(--ring-light), var(--ring-mid) 60%, transparent 72%);
  }
  .front-author {
    position: absolute; left: 0; right: 0; bottom: 38px; text-align: center;
    font-family: "Advent Pro", sans-serif; font-weight: 400;
    font-size: 24px; letter-spacing: 2px; color: var(--ink-soft);
  }

  /* Back */
  .bio-block { position: absolute; left: 30px; top: 40px; width: 230px; }
  .bio-name {
    font-family: "Tinos", serif; font-weight: 400;
    font-size: 20px; color: var(--ink); margin-bottom: 8px;
  }
  .bio-text {
    font-family: "Tinos", serif; font-style: italic;
    font-size: 8.5px; line-height: 1.55; color: var(--ink-soft); text-align: justify;
  }
  .bio-photo {
    position: absolute; right: 30px; top: 44px; width: 96px; height: 118px;
    background: linear-gradient(180deg, #b7ae9f, var(--photo-tone));
    border: 2px solid #ffffff;
  }
  .testimonials {
    position: absolute; right: 30px; top: 200px; width: 320px;
    font-family: "Tinos", serif; font-size: 16px; color: var(--ink); text-align: right;
  }
  .testimonial { margin-bottom: 22px; line-height: 1.35; }
  .testimonial cite { display: block; font-style: normal; padding-right: 8px; }
  .back-rings-photo {
    position: absolute; left: 30px; right: 20px; bottom: 20px; height: 90px; border-radius: 50%;
    background: radial-gradient(ellipse at 60% 50%, var(--ring-light), var(--ring-mid) 60%, transparent 72%);
  }

  /* Spine */
  .spine-text {
    position: absolute; left: 50%; top: 20px;
    writing-mode: vertical-rl;
    transform: translateX(-50%);
    white-space: nowrap;
  }
  .spine-title { font-size: 34px; letter-spacing: 2px; }
  .spine-author {
    font-family: "Advent Pro", sans-serif; font-weight: 400;
    font-size: 13px; letter-spacing: 1.5px; color: var(--ink-soft);
    margin-top: 14px;
  }
</style>
</head>
<body>
  <main class="book-spread">
    <section class="panel back-cover">
      <div class="bio-block">
        <h2 class="bio-name">Megan Trabert PhD</h2>
        <p class="bio-text">Megan Trabert has broad experience from school to university settings, with availability to do motivational talks at corporate, church, educational, or community events, national conventions and retreats on topics such as improving relationships, self-care, spirituality, and navigating the challenges of infidelity.</p>
      </div>
      <div class="bio-photo" role="img" aria-label="Author portrait photograph"></div>
      <div class="testimonials">
        <blockquote class="testimonial">“This book has saved my marriage”<cite>Nolan Brisk.</cite></blockquote>
        <blockquote class="testimonial">“It changed all my paradigms about what being married means”<cite>Jesse Harlow.</cite></blockquote>
        <blockquote class="testimonial">“Thanks to this book which gave me the strength to continue the journey of marriage”<cite>Abel Thornwood.</cite></blockquote>
      </div>
      <div class="back-rings-photo" role="img" aria-label="Photograph of silver wedding rings"></div>
    </section>

    <section class="panel spine">
      <div class="spine-text">
        <span class="silver-text spine-title">OPEN ORCHARD</span>
        <span class="spine-author">DR. MEGAN TRABERT PHD</span>
      </div>
    </section>

    <section class="panel front-cover">
      <h1 class="front-title silver-text">
        <span class="line-one">OPEN</span>
        <span class="line-two">ORCHARD</span>
      </h1>
      <p class="front-tagline">Peace, Love and Happiness</p>
      <div class="rings-photo" role="img" aria-label="Photograph of two silver wedding rings"></div>
      <p class="front-author">DR. MEGAN TRABERT PHD</p>
    </section>
  </main>
</body>
</html>
```